Optimization existing Business Card

I need a revision of the business card, incl. Logo Design. I am a freelancer and have my headquarters in Berlin. I develop business consulting solutions for banks, insurance and StartUp Companies. I want a simple design of the business card. The final design should professionalism and commitment and openness to communicate. I'm open minded in addition to optimizing the existing logo / business card as well on a new idea / proposal for the logo. Idea would be for example the logo of this page: http://morvale-advisory.example.

Target Market(s)

Consulting, Banking, Investment Banking

Industry/Entity Type

Business

Contact Information for Business Card

siehe Anhang (please take a look into the attachments, important)

Font styles to use
Sans Serif

Requirements
Must have
• Please look at my specifications exactly !! (Please see my specifications), CEO Founder not
Should not have
• No gradient !! (No overarching color gradient)

```html
<!DOCTYPE html>
<html lang="en">
<head>
<meta charset="utf-8">
<title>clearpoint – Business Card</title>
<link rel="stylesheet" href="https://fonts.googleapis.com/css2?family=Roboto:wght@300;400;500&display=swap">
<style>
  :root {
    --backdrop: #606060;
    --paper: #ececec;
    --ink: #2e2e2e;
    --ink-soft: #4a2c2c;
    --accent: #29b0e0;
    --rule: #8a8a8a;
  }
  * { box-sizing: border-box; margin: 0; padding: 0; }
  html, body { width: 1200px; height: 1200px; overflow: hidden; }
  body {
    background: var(--backdrop);
    font-family: "Roboto", Arial, sans-serif;
    position: relative;
  }
  .card {
    position: absolute;
    left: 250px;
    width: 700px;
    height: 420px;
    background: var(--paper);
    box-shadow: 4px 4px 0 #3c3c3c;
    overflow: hidden;
  }
  .card--front { top: 150px; }
  .card--back { top: 630px; display: flex; align-items: center; justify-content: center; }

  .brand {
    display: flex;
    align-items: center;
    gap: 14px;
    font-weight: 500;
    color: var(--accent);
    letter-spacing: -1px;
  }
  .brand__dot {
    border: 4px solid var(--ink);
    border-radius: 50%;
  }
  .card--front .brand { position: absolute; left: 40px; top: 120px; font-size: 52px; }
  .card--front .brand__dot { width: 30px; height: 30px; }
  .card--back .brand { font-size: 58px; }
  .card--back .brand__dot { width: 34px; height: 34px; }

  .divider {
    position: absolute;
    left: 360px;
    top: 20px;
    width: 1px;
    height: 320px;
    background: var(--rule);
  }
  .contact-line {
    display: flex;
    align-items: center;
    gap: 8px;
    color: var(--ink-soft);
  }
  .contact-line svg { flex: none; }
  .email { position: absolute; left: 26px; top: 258px; font-size: 18px; font-weight: 300; }

  .person { position: absolute; left: 392px; top: 60px; }
  .person__name { font-size: 21px; font-weight: 400; color: var(--ink); }
  .person__role { font-size: 20px; font-weight: 300; color: var(--accent); margin-top: 4px; }

  .phones { position: absolute; left: 392px; top: 250px; display: grid; gap: 6px; font-size: 21px; font-weight: 300; }

  .address-band {
    position: absolute;
    left: 0; right: 0; bottom: 0;
    height: 62px;
    background: var(--accent);
    color: #fff;
    font-size: 19px;
    font-weight: 400;
    display: flex;
    align-items: center;
    justify-content: center;
  }
</style>
</head>
<body>
  <section class="card card--front" aria-label="Business card front">
    <div class="brand"><span class="brand__dot"></span>clearpoint</div>

    <div class="contact-line email">
      <svg width="14" height="12" viewBox="0 0 14 12" aria-hidden="true">
        <rect width="14" height="12" rx="2" fill="var(--accent)"/>
        <path d="M3 4 L7 7 L11 4" stroke="#fff" stroke-width="1.2" fill="none"/>
      </svg>
      lh@hartwig-consulting.example
    </div>

    <div class="divider"></div>

    <div class="person">
      <p class="person__name">Lena Hartwig</p>
      <p class="person__role">CEO</p>
    </div>

    <div class="phones">
      <div class="contact-line">
        <svg width="16" height="16" viewBox="0 0 16 16" aria-hidden="true">
          <rect width="16" height="16" rx="2" fill="var(--accent)"/>
          <path d="M5 3 L7 5 L6 6.5 C7 8.5 8 9.5 9.5 10 L11 9 L13 11 L11.5 13 C7.5 12.5 3.5 8.5 3 4.5 Z" fill="#fff"/>
        </svg>
        +49 (0) 30555012345
      </div>
      <div class="contact-line">
        <svg width="16" height="16" viewBox="0 0 16 16" aria-hidden="true">
          <rect width="16" height="16" rx="2" fill="var(--accent)"/>
          <rect x="5.5" y="3" width="5" height="10" rx="1" fill="#fff"/>
          <rect x="6.5" y="4.5" width="3" height="5.5" fill="var(--accent)"/>
        </svg>
        +49 (0) 17655598120
      </div>
    </div>

    <div class="address-band">Lindenweg 48, 10115 Berlin, Germany</div>
  </section>

  <section class="card card--back" aria-label="Business card back">
    <div class="brand"><span class="brand__dot"></span>clearpoint</div>
  </section>
</body>
</html>
```